Design home page for SME Tidewell

WordPress homepage for SME Tidewell.
Will use GeneratePress, and the theme will be a child theme of Generate Press.
Logo attached.
SME Tidewell is a business that advises Small to Medium Businesses towards success.

```html
<!DOCTYPE html>
<html lang="en">
<head>
<meta charset="utf-8">
<title>SME Tidewell – Home</title>
<link href="https://fonts.googleapis.com/css2?family=Raleway:wght@400;500;600;700&family=Open+Sans:wght@400;600;700&display=swap" rel="stylesheet">
<style>
:root{
  --ink:#1f2a3a;
  --text:#5b6473;
  --slate:#4b5567;
  --navy:#2f4a72;
  --blue:#4a8fe0;
  --blue-soft:#dde9f8;
  --steel:#3d5f8f;
  --footer:#2e333d;
  --footer-deep:#262a33;
  --line:#d9dee6;
  --white:#ffffff;
}
*{box-sizing:border-box;margin:0;padding:0}
html,body{width:1200px;height:3332px;overflow:hidden}
body{font-family:"Open Sans",sans-serif;color:var(--text);background:var(--white);position:relative;font-size:13px;line-height:1.6}
h1,h2,h3,h4,.brand{font-family:"Raleway",sans-serif;color:var(--ink)}
.abs{position:absolute}
.placeholder{position:absolute;border-radius:8px}

/* header */
.site-header{position:absolute;left:0;top:0;width:1200px;height:100px;z-index:3}
.brand{position:absolute;left:120px;top:24px;display:flex;align-items:center;gap:10px;font-size:30px;font-weight:700;color:var(--navy);letter-spacing:1px}
.brand-mark{width:26px;height:26px;background:var(--navy)}
.call{position:absolute;left:1030px;top:14px;font-size:11px;color:var(--ink);display:flex;align-items:center;gap:6px}
.call-dot{width:18px;height:18px;border-radius:50%;background:var(--blue);display:flex;align-items:center;justify-content:center}
.nav{position:absolute;left:740px;top:44px;display:flex;gap:6px}
.nav a{font-size:11px;font-weight:600;color:var(--ink);text-decoration:none;padding:6px 14px;border-radius:14px;letter-spacing:.5px}
.nav a.active{background:var(--white);box-shadow:0 2px 8px rgba(0,0,0,.12)}

/* hero */
.hero{position:absolute;left:0;top:0;width:1200px;height:600px;background:linear-gradient(90deg,#fafbfc,#eef1f5)}
.hero-art{left:560px;top:0;width:640px;height:500px;background:radial-gradient(circle at 60% 45%,#f2b98f 0,#e7cbb2 30%,#dde3ea 65%,transparent 80%)}
.hero-copy{position:absolute;left:120px;top:108px}
.eyebrow{font-size:13px;font-weight:700;color:var(--ink);letter-spacing:1px}
.hero-copy h1{font-size:42px;line-height:1.2;font-weight:600;margin-top:4px}
.hero-copy p{width:330px;margin-top:22px;font-size:13px}
.btns{display:flex;gap:14px;margin-top:26px}
.btn{font-size:11px;font-weight:700;letter-spacing:.5px;padding:9px 20px;border-radius:20px}
.btn-fill{background:var(--navy);color:var(--white)}
.btn-line{border:1px solid var(--navy);color:var(--navy);background:var(--white)}
.hero-wave{position:absolute;left:0;top:430px}

/* features */
.feature{position:absolute;top:644px;height:210px;background:var(--white);border:1px solid var(--line);border-radius:4px;padding:26px 24px;box-shadow:0 4px 18px rgba(0,0,0,.05)}
.feature h3{font-size:18px;font-weight:600;margin:14px 0 6px}
.feature p{font-size:12px}
.feature.highlight{background:var(--blue);border-color:var(--blue);top:620px;height:240px;color:#eaf2fd}
.feature.highlight h3{color:var(--white)}
.feature .more{display:inline-block;margin-top:16px;background:var(--white);color:var(--navy);font-size:10px;font-weight:700;padding:8px 18px;border-radius:16px}

/* about */
.about-art{left:100px;top:940px;width:440px;height:400px;background:radial-gradient(circle at 55% 55%,#f7dc6a 0,#e9e7d8 35%,#f2f4f7 65%,transparent 80%)}
.about{position:absolute;left:608px;top:966px;width:470px}
.label{font-size:13px;font-weight:600;color:var(--ink);letter-spacing:1px}
.about h2{font-size:36px;line-height:1.15;font-weight:600;margin-top:6px}
.about p{margin-top:14px;font-size:12px}
.accordion{margin-top:18px;display:flex;flex-direction:column;gap:8px}
.acc{border:1px solid var(--line);border-radius:3px;font-size:11px;padding:7px 14px;display:flex;justify-content:space-between;color:var(--ink)}
.acc.open{background:var(--blue-soft)}

/* services */
.services{position:absolute;left:0;top:1380px;width:1200px;height:720px;background:var(--slate)}
.services .head{text-align:center;margin-top:44px}
.services .label,.services h2{color:var(--white)}
.services h2{font-size:36px;font-weight:600;margin-top:2px}
.services .intro{width:760px;margin:8px auto 0;color:#d6dbe3;font-size:12px;text-align:center}
.service{position:absolute;width:236px;height:200px;border:1px solid #7b8496;padding:24px 22px;color:#d3d8e0;font-size:11px;line-height:1.55}
.service h4{color:var(--white);font-size:15px;font-weight:600;margin:10px 0 6px}
.service .rm{display:block;margin-top:12px;font-weight:700;color:var(--white);font-size:10px}
.service.raised{background:var(--white);border-color:var(--white);box-shadow:0 10px 26px rgba(0,0,0,.25);color:var(--text)}
.service.raised h4,.service.raised .rm{color:var(--ink)}
.ico{width:32px;height:32px}

/* contact */
.contact{position:absolute;left:120px;top:2150px}
.contact h2{font-size:36px;font-weight:500;margin-top:2px}
.form{position:absolute;left:120px;top:2250px;width:620px;display:grid;grid-template-columns:300px 300px;gap:8px 18px}
.field{border:1px solid var(--line);height:38px;font-size:11px;padding:10px 12px;color:#8a93a1}
.field.msg{grid-row:span 2;height:84px}
.submit{background:var(--navy);color:var(--white);font-size:11px;font-weight:700;text-align:center;padding:11px;letter-spacing:.5px}
.contact-art{left:790px;top:2090px;width:300px;height:390px;background:radial-gradient(circle at 50% 50%,#ea8a5a 0,#f1c5a8 35%,#e9eef4 68%,transparent 82%)}

/* testimonials */
.quote-block{position:absolute;left:600px;top:2540px;width:520px;color:#dfe7f2}
.quote-block .label{color:var(--white)}
.quote-block h2{color:var(--white);font-size:36px;font-weight:500;margin-top:2px}
.quote-block .mark{font-size:42px;color:var(--white);line-height:1;margin-top:10px;font-family:"Raleway",sans-serif}
.quote-block p{font-size:12px;margin-top:4px}
.author{display:flex;align-items:center;gap:14px;margin-top:18px}
.avatar{width:50px;height:50px;border-radius:50%;background:#8fa7c6}
.author strong{display:block;color:var(--white);font-family:"Raleway",sans-serif;font-size:15px;line-height:1.3}
.author span{font-size:11px}
.testi-art{left:160px;top:2540px;width:380px;height:300px;background:radial-gradient(ellipse at 50% 60%,#c98b5f 0,#8fa3bd 45%,#5a78a2 75%,transparent 90%)}

/* footer */
.site-footer{position:absolute;left:0;top:2860px;width:1200px;height:472px;background:var(--footer);color:#b9c0cc}
.f-brand{position:absolute;left:120px;top:80px;width:300px}
.f-brand .brand{position:static;color:var(--white)}
.f-brand .brand-mark{background:var(--white)}
.f-brand p{margin-top:20px;font-size:12px}
.socials{display:flex;gap:10px;margin-top:20px}
.socials i{width:28px;height:28px;border:1px solid #b9c0cc;border-radius:50%;display:block}
.f-col{position:absolute;top:124px;border-left:1px solid #59606d;padding-left:18px;height:190px}
.f-col h4{color:var(--white);font-size:17px;font-weight:600;margin-bottom:14px}
.f-col li{list-style:none;font-size:12px;margin-bottom:6px}
.copyright{position:absolute;left:0;bottom:0;width:1200px;height:62px;background:var(--footer-deep);text-align:center;line-height:62px;font-size:12px}
</style>
</head>
<body>

<section class="hero">
  <div class="placeholder hero-art abs" role="img" aria-label="Illustration of two business people relaxing in orange armchairs with laptops"></div>
  <div class="hero-copy">
    <div class="eyebrow">GREAT</div>
    <h1>Explorer of<br>The Master-Builder</h1>
    <p>We guide small and medium businesses with clear plans, steady advice and practical growth steps.</p>
    <div class="btns"><span class="btn btn-fill">GET STARTED</span><span class="btn btn-line">CONTACT US</span></div>
  </div>
  <svg class="hero-wave" width="1200" height="170" viewBox="0 0 1200 170">
    <path d="M0 110 C260 200 520 80 780 100 C960 115 1080 40 1200 0 L1200 170 L0 170Z" fill="#ffffff"/>
    <path d="M0 110 C260 200 520 80 780 100 C960 115 1080 40 1200 0 L1200 24 C1090 70 960 135 780 124 C520 108 260 220 0 134Z" fill="#4b5567"/>
  </svg>
</section>

<header class="site-header">
  <div class="brand"><span class="brand-mark"></span>SME TIDEWELL</div>
  <div class="call"><span class="call-dot"><svg width="10" height="10" viewBox="0 0 24 24"><path d="M6.6 10.8a15 15 0 0 0 6.6 6.6l2.2-2.2a1 1 0 0 1 1-.25 11.4 11.4 0 0 0 3.6.6 1 1 0 0 1 1 1V20a1 1 0 0 1-1 1A17 17 0 0 1 3 4a1 1 0 0 1 1-1h3.5a1 1 0 0 1 1 1c0 1.250.2 2.45.6 3.6a1 1 0 0 1-.25 1z" fill="#fff"/></svg></span>Call Us: +1 (555) 014 2290</div>
  <nav class="nav"><a class="active">HOME</a><a>ABOUT US</a><a>SERVICE</a><a>CONTACT US</a></nav>
</header>

<article class="feature" style="left:112px;width:308px">
  <svg class="ico" viewBox="0 0 32 32" fill="none" stroke="#1f2a3a" stroke-width="1.6"><rect x="5" y="9" width="22" height="16" rx="2"/><path d="M12 9V6h8v3M5 16h22"/></svg>
  <h3>Finibus Bonorum</h3>
  <p>Sed ut perspiciatis unde omnis iste natus error sit voluptatem accusantium doloremque.</p>
</article>
<article class="feature highlight" style="left:448px;width:300px">
  <svg class="ico" viewBox="0 0 32 32" fill="none" stroke="#fff" stroke-width="1.6"><circle cx="16" cy="12" r="6"/><path d="M6 27c2-6 18-6 20 0"/></svg>
  <h3>Finibus Bonorum</h3>
  <p>Sed ut perspiciatis unde omnis iste natus error sit voluptatem accusantium doloremque laudantium.</p>
  <span class="more">READ MORE</span>
</article>
<article class="feature" style="left:768px;width:312px">
  <svg class="ico" viewBox="0 0 32 32" fill="none" stroke="#1f2a3a" stroke-width="1.6"><path d="M6 26V14l10-8 10 8v12z"/><path d="M13 26v-7h6v7"/></svg>
  <h3>Finibus Bonorum</h3>
  <p>Sed ut perspiciatis unde omnis iste natus error sit voluptatem accusantium doloremque.</p>
</article>

<div class="placeholder about-art abs" role="img" aria-label="Illustration of two businessmen shaking hands beside a large light bulb and a potted plant"></div>
<section class="about">
  <div class="label">ABOUT US</div>
  <h2>We Are Here<br>For Business Solution Idea</h2>
  <p>Sed ut perspiciatis unde omnis iste natus error sit voluptatem accusantium doloremque laudantium, totam rem aperiam, eaque ipsa quae ab illo inventore veritatis et quasi architecto beatae vitae dicta sunt explicabo. Nemo enim ipsam voluptatem quia voluptas sit aspernatur aut odit aut fugit, sed quia consequuntur magni dolores eos qui ratione voluptatem sequi nesciunt.</p>
  <div class="accordion">
    <div class="acc open"><span>Duis in culpa qui officia deserunt mollit anim id est laborum?</span><span>⌃</span></div>
    <div class="acc"><span>Duis in culpa qui officia deserunt mollit anim id est laborum?</span><span>⌄</span></div>
    <div class="acc"><span>Duis in culpa qui officia deserunt mollit anim id est laborum?</span><span>⌄</span></div>
  </div>
</section>

<section class="services">
  <div class="head">
    <div class="label">OUR SERVICES</div>
    <h2>What We Provide</h2>
    <p class="intro">Sed ut perspiciatis unde omnis iste natus error sit voluptatem accusantium doloremque laudantium, totam rem aperiam, eaque ipsa quae ab illo inventore veritatis et quasi architecto beatae vitae dicta sunt explicabo.</p>
  </div>
</section>
<article class="service raised" style="left:104px;top:1570px"><svg class="ico" viewBox="0 0 32 32" fill="none" stroke="#1f2a3a" stroke-width="1.6"><circle cx="16" cy="11" r="5"/><path d="M7 26c2-6 16-6 18 0"/></svg><h4>Consectetur Adipiscing</h4>Sed ut perspiciatis unde omnis iste natus error sit voluptatem accusantium.<span class="rm">READ MORE</span></article>
<article class="service" style="left:348px;top:1578px"><svg class="ico" viewBox="0 0 32 32" fill="none" stroke="#fff" stroke-width="1.6"><rect x="6" y="8" width="20" height="16" rx="2"/><path d="M6 14h20"/></svg><h4>Consectetur Adipiscing</h4>Sed ut perspiciatis unde omnis iste natus error sit voluptatem accusantium.<span class="rm">READ MORE</span></article>
<article class="service" style="left:592px;top:1578px"><svg class="ico" viewBox="0 0 32 32" fill="none" stroke="#fff" stroke-width="1.6"><path d="M6 24l7-8 5 5 8-10"/><path d="M20 11h6v6"/></svg><h4>Consectetur Adipiscing</h4>Sed ut perspiciatis unde omnis iste natus error sit voluptatem accusantium.<span class="rm">READ MORE</span></article>
<article class="service" style="left:836px;top:1578px"><svg class="ico" viewBox="0 0 32 32" fill="none" stroke="#fff" stroke-width="1.6"><circle cx="16" cy="16" r="10"/><path d="M16 10v6l4 3"/></svg><h4>Consectetur Adipiscing</h4>Sed ut perspiciatis unde omnis iste natus error sit voluptatem accusantium.<span class="rm">READ MORE</span></article>
<article class="service" style="left:104px;top:1786px"><svg class="ico" viewBox="0 0 32 32" fill="none" stroke="#fff" stroke-width="1.6"><path d="M6 8h20v13H14l-6 5v-5H6z"/></svg><h4>Consectetur Adipiscing</h4>Sed ut perspiciatis unde omnis iste natus error sit voluptatem accusantium.<span class="rm">READ MORE</span></article>
<article class="service" style="left:348px;top:1786px"><svg class="ico" viewBox="0 0 32 32" fill="none" stroke="#fff" stroke-width="1.6"><path d="M16 5l9 5v8c0 5-4 8-9 9-5-1-9-4-9-9v-8z"/></svg><h4>Consectetur Adipiscing</h4>Sed ut perspiciatis unde omnis iste natus error sit voluptatem accusantium.<span class="rm">READ MORE</span></article>
<article class="service" style="left:592px;top:1786px"><svg class="ico" viewBox="0 0 32 32" fill="none" stroke="#fff" stroke-width="1.6"><circle cx="12" cy="12" r="4"/><circle cx="22" cy="14" r="3"/><path d="M4 26c1-5 15-5 16 0M18 24c1-3 9-3 10 0"/></svg><h4>Consectetur Adipiscing</h4>Sed ut perspiciatis unde omnis iste natus error sit voluptatem accusantium.<span class="rm">READ MORE</span></article>
<article class="service" style="left:836px;top:1786px"><svg class="ico" viewBox="0 0 32 32" fill="none" stroke="#fff" stroke-width="1.6"><path d="M8 6h16v20H8z"/><path d="M12 12h8M12 17h8M12 22h5"/></svg><h4>Consectetur Adipiscing</h4>Sed ut perspiciatis unde omnis iste natus error sit voluptatem accusantium.<span class="rm">READ MORE</span></article>

<svg class="abs" style="left:0;top:2010px" width="1200" height="120" viewBox="0 0 1200 120">
  <path d="M0 0 H1200 V40 C900 130 400 30 0 90Z" fill="#4b5567"/>
  <path d="M0 90 C400 30 900 130 1200 40 V60 C900 150 400 50 0 110Z" fill="#4a8fe0"/>
  <path d="M0 110 C400 50 900 150 1200 60 V120 H0Z" fill="#ffffff"/>
</svg>

<div class="placeholder contact-art abs" role="img" aria-label="Illustration of a cheering businessman with raised arms sitting on an orange chair with a laptop"></div>
<section class="contact">
  <div class="label">CONTACT US</div>
  <h2>You Have Any Question</h2>
</section>
<form class="form">
  <div class="field">Name</div>
  <div class="field msg">Comments</div>
  <div class="field">Email</div>
  <div class="field">Phone</div>
  <div class="submit">SUBMIT</div>
</form>

<svg class="abs" style="left:0;top:2400px" width="1200" height="470" viewBox="0 0 1200 470">
  <path d="M0 110 C300 40 700 100 1200 30 V470 H0Z" fill="#3d5f8f"/>
</svg>
<div class="placeholder testi-art abs" role="img" aria-label="Illustration of a cartoon businessman in glasses working at a laptop on a desk"></div>
<section class="quote-block">
  <div class="label">TESTIMONIALS</div>
  <h2>What Our Client Say</h2>
  <div class="mark">“</div>
  <p>Sed ut perspiciatis unde omnis iste natus error sit voluptatem accusantium doloremque laudantium, totam rem aperiam, eaque ipsa quae ab illo inventore veritatis et quasi architecto beatae vitae dicta sunt explicabo.</p>
  <div class="author"><div class="avatar" role="img" aria-label="Client portrait"></div><div><strong>Dana Whitlow</strong><span>Consultant</span></div></div>
</section>

<footer class="site-footer">
  <div class="f-brand">
    <div class="brand"><span class="brand-mark"></span>SME TIDEWELL</div>
    <p>Sed ut perspiciatis unde omnis iste natus error sit voluptatem accusantium doloremque laudantium, totam rem aperiam, eaque ipsa quae ab illo.</p>
    <div class="socials"><i></i><i></i><i></i><i></i></div>
  </div>
  <div class="f-col" style="left:500px"><h4>Quick Links</h4><ul><li>Home</li><li>About Us</li><li>Services</li><li>Contact Us</li></ul></div>
  <div class="f-col" style="left:670px"><h4>Services</h4><ul><li>Consectetur Adipiscing</li><li>Doloremque Laudantium</li><li>Finibus Bonorum</li><li>Voluptatem Sequi</li></ul></div>
  <div class="f-col" style="left:860px"><h4>Contact Us</h4><ul><li>48 Harbor Lane,<br>Westbury 20415</li><li>+1 (555) 014 2290</li><li>hello@smetidewell.example</li></ul></div>
  <div class="copyright">Copyright © 2024 SME Tidewell. All Rights Reserved.</div>
</footer>

</body>
</html>
```